business card design

i would like business cards designed. My business provides trade qualified personnel to the mining industry to work on heavy mobile equipment.
please put a excavator(digger) in the background in one design and have one design without so i can compare the difference.
also add info:
my logo(attached) and "mobile equipment repair and maintenance"
name: Derek Holloway
address: 57 Tarrowby RD Carmel Perth WA.
mobile: 0438120957
email: derek@ironvalemx.com

```html
<!DOCTYPE html>
<html lang="en">
<head>
<meta charset="utf-8">
<title>Ironvale Maintenance Services – Business Cards</title>
<link href="https://fonts.googleapis.com/css2?family=Oswald:wght@500;700&family=Roboto:wght@400;500&display=swap" rel="stylesheet">
<style>
  :root{
    --page:#ececea;
    --card:#ffffff;
    --ink:#1f2328;
    --navy:#2a2f37;
    --royal:#3f6fc2;
    --sky:#12a9e8;
    --sky-light:#5cc6f2;
    --steel:#6d7078;
    --ghost:#d3d5d8;
  }
  *{box-sizing:border-box;margin:0;padding:0}
  html,body{width:1200px;height:900px;overflow:hidden;background:var(--page)}
  .sheet{
    width:1200px;height:900px;display:flex;align-items:center;justify-content:center;gap:50px;
  }
  .card{
    position:relative;width:540px;height:309px;background:var(--card);overflow:hidden;
    box-shadow:0 6px 18px rgba(0,0,0,.14);
  }
  .card svg.art{position:absolute;inset:0}

  /* brand wordmark */
  .brand{position:absolute;text-align:left;color:var(--ink);z-index:1}
  .brand-name{
    font-family:"Oswald",sans-serif;font-weight:700;font-size:34px;letter-spacing:2px;line-height:1;color:var(--ink);
  }
  .brand-sub{
    font-family:"Roboto",sans-serif;font-weight:500;font-size:7.5px;letter-spacing:1.1px;color:var(--ink);margin-top:3px;
  }

  /* front */
  .front .brand{top:28px;right:34px}
  .tagline{
    position:absolute;left:34px;top:96px;z-index:1;
    font-family:"Oswald",sans-serif;font-weight:700;font-size:21px;line-height:30px;letter-spacing:.4px;color:var(--royal);
    text-transform:uppercase;white-space:nowrap;
  }
  .tagline-rule{position:absolute;left:34px;top:132px;width:290px;height:2px;background:var(--royal)}

  /* back */
  .back .brand{top:22px;left:30px}
  .machine{position:absolute;right:26px;top:12px;width:200px;height:110px;border-radius:6px;
    background:radial-gradient(ellipse at 55% 55%, var(--ghost), rgba(255,255,255,0) 70%)}
  .holder{
    position:absolute;left:30px;top:178px;
    font-family:"Roboto",sans-serif;font-weight:500;font-size:19px;letter-spacing:1px;color:#fff;text-transform:uppercase;
  }
  .contacts{position:absolute;left:30px;top:216px;list-style:none}
  .contacts li{
    display:flex;align-items:center;gap:9px;height:24px;
    font-family:"Roboto",sans-serif;font-size:12.5px;color:#e6e8eb;
  }
  .contacts .icon{width:15px;height:15px;background:var(--royal);border-radius:2px;display:flex;align-items:center;justify-content:center}
</style>
</head>
<body>
<main class="sheet">

  <section class="card front" aria-label="Card front">
    <svg class="art" width="540" height="309" viewBox="0 0 540 309" aria-hidden="true">
      <path d="M0 309 L0 290 C200 270 380 230 540 110 L540 309 Z" fill="var(--sky)"/>
      <path d="M0 309 L0 300 C220 285 400 250 540 150 L540 309 Z" fill="var(--sky-light)" opacity=".55"/>
      <path d="M150 309 C300 270 430 230 540 180" stroke="var(--steel)" stroke-width="12" fill="none"/>
      <path d="M0 280 C200 260 380 220 540 100" stroke="var(--royal)" stroke-width="3" fill="none"/>
      <path d="M380 196 C440 165 495 130 540 90 L540 102 C495 140 440 175 380 196 Z" fill="var(--royal)"/>
    </svg>
    <div class="brand">
      <div class="brand-name">IRONVALE</div>
      <div class="brand-sub">MAINTENANCE SERVICES PTY LTD</div>
    </div>
    <div class="tagline">Mobile Equipment Repair and Maintenance</div>
    <div class="tagline-rule"></div>
  </section>

  <section class="card back" aria-label="Card back">
    <svg class="art" width="540" height="309" viewBox="0 0 540 309" aria-hidden="true">
      <path d="M0 130 C140 118 300 128 540 170 L540 309 L0 309 Z" fill="var(--navy)"/>
      <path d="M0 124 C150 110 320 118 540 162 L540 172 C320 132 150 124 0 136 Z" fill="var(--royal)"/>
      <path d="M60 134 C120 124 180 124 230 132 L200 142 C150 136 110 136 60 140 Z" fill="var(--royal)" opacity=".9"/>
      <path d="M150 128 C200 122 240 124 270 130 L245 138 C210 133 180 132 150 134 Z" fill="var(--sky)"/>
    </svg>
    <div class="brand">
      <div class="brand-name">IRONVALE</div>
      <div class="brand-sub">MAINTENANCE SERVICES PTY LTD</div>
    </div>
    <div class="machine" role="img" aria-label="Faint excavator illustration in light grey"></div>
    <div class="holder">Derek Holloway</div>
    <ul class="contacts">
      <li>
        <span class="icon"><svg width="11" height="11" viewBox="0 0 12 12" aria-hidden="true"><path d="M6 1 L11 6 H9.5 V11 H7 V8 H5 V11 H2.5 V6 H1 Z" fill="#fff"/></svg></span>
        57 Tarrowby RD, Carmel Perth, WA.
      </li>
      <li>
        <span class="icon"><svg width="11" height="11" viewBox="0 0 12 12" aria-hidden="true"><rect x="3.5" y="1" width="5" height="10" rx="1" fill="#fff"/><rect x="4.5" y="2.3" width="3" height="6" fill="var(--royal)"/></svg></span>
        0438120957
      </li>
      <li>
        <span class="icon"><svg width="11" height="11" viewBox="0 0 12 12" aria-hidden="true"><rect x="1" y="3" width="10" height="7" fill="#fff"/><path d="M1 3 L6 7 L11 3" stroke="var(--royal)" stroke-width="1" fill="none"/></svg></span>
        derek@ironvalemx.com
      </li>
    </ul>
  </section>

</main>
</body>
</html>
```